Postcards for Upscale Landscaping Company
Harbor Fern KT
Postcards for Upscale Landscaping Company  - Home and Garden
Creative Brief
Home and Garden
High end homeowners in the $2m+ range. Owner specializing in fine gardening and hedge/topiary trimming.
Need a design for a 5x7 postcard. Front with stamp will just include the logo and and mission statement, name, contact info etc. as on current business card to be submitted.
Tbrantley Tbrantley
I’m not sure we have the card in that file format. I’ll work on it and get Bach to you. Thanks.
sarvesh sarvesh
Hi, Please upload your logo in Ai or PNG file format.

```html
<!DOCTYPE html>
<html lang="en">
<head>
<meta charset="utf-8">
<title>Harbor Fern KT – Postcard</title>
<link href="https://fonts.googleapis.com/css2?family=Oswald:wght@300;400&display=swap" rel="stylesheet">
<style>
  :root {
    --paper: #ffffff;
    --coral: #e1603d;
    --slate: #4b4f4b;
    --ink: #2e2e2e;
    --brand-red: #b3262b;
    --ghost: #eeeeee;
  }
  html, body {
    margin: 0;
    padding: 0;
    overflow: hidden;
    background: var(--paper);
  }
  .postcard {
    position: relative;
    width: 1200px;
    height: 869px;
    overflow: hidden;
    background: var(--paper);
    font-family: "Oswald", "Arial Narrow", sans-serif;
  }
  .backdrop {
    position: absolute;
    inset: 0;
  }
  .brand {
    position: absolute;
    left: 110px;
    top: 60px;
    width: 320px;
    text-align: center;
  }
  .brand-dot {
    width: 120px;
    height: 120px;
    margin: 0 auto 22px;
    border-radius: 50%;
    background: var(--brand-red);
  }
  .brand-name {
    margin: 0;
    font-weight: 400;
    font-size: 36px;
    letter-spacing: 1px;
    text-transform: uppercase;
    color: var(--ink);
    line-height: 1;
    white-space: nowrap;
  }
  .brand-ghost {
    position: absolute;
    left: 310px;
    bottom: 14px;
    margin: 0;
    font-weight: 400;
    font-size: 84px;
    letter-spacing: 2px;
    text-transform: uppercase;
    color: var(--ghost);
    line-height: 1;
    white-space: nowrap;
  }
  .offer {
    position: absolute;
    left: 112px;
    top: 560px;
    margin: 0;
    font-weight: 300;
    font-size: 48px;
    line-height: 1.15;
    color: var(--ink);
    white-space: nowrap;
  }
</style>
</head>
<body>
<main class="postcard">
  <svg class="backdrop" width="1200" height="869" viewBox="0 0 1200 869">
    <defs>
      <linearGradient id="roses" x1="0" y1="0" x2="1" y2="1">
        <stop offset="0" stop-color="#c9cfa8"/>
        <stop offset="0.5" stop-color="#e8c25a"/>
        <stop offset="1" stop-color="#b99a62"/>
      </linearGradient>
      <linearGradient id="hedges" x1="0" y1="0" x2="0" y2="1">
        <stop offset="0" stop-color="#3f5f2e"/>
        <stop offset="0.55" stop-color="#5f8a45"/>
        <stop offset="1" stop-color="#86ad5a"/>
      </linearGradient>
      <linearGradient id="lighthouse" x1="0" y1="0" x2="0" y2="1">
        <stop offset="0" stop-color="#a9c6de"/>
        <stop offset="0.6" stop-color="#d9e4ea"/>
        <stop offset="1" stop-color="#4f6e3a"/>
      </linearGradient>
      <linearGradient id="borders" x1="0" y1="0" x2="0" y2="1">
        <stop offset="0" stop-color="#3d6033"/>
        <stop offset="0.55" stop-color="#8e8a4e"/>
        <stop offset="1" stop-color="#d0608a"/>
      </linearGradient>
      <linearGradient id="fadedTower" x1="0" y1="0" x2="1" y2="0">
        <stop offset="0" stop-color="#e1603d" stop-opacity="0"/>
        <stop offset="1" stop-color="#f08c6c" stop-opacity="0.55"/>
      </linearGradient>
    </defs>

    <polygon class="coral-field" points="470,0 1200,0 1200,869 1010,869" fill="var(--coral)"/>
    <rect class="coral-photo" x="1000" y="40" width="200" height="829" fill="url(#fadedTower)"
          role="img" aria-label="Faded photo of a lighthouse tinted into the coral field"/>
    <polygon class="slate-corner" points="0,600 0,869 290,869" fill="var(--slate)"/>

    <g class="collage">
      <polygon class="collage-frame" points="780,35 1090,345 780,655 470,345" fill="var(--paper)"/>
      <polygon points="780,60 918,198 780,336 642,198" fill="url(#roses)"
               role="img" aria-label="Photo of yellow roses in bloom"/>
      <polygon points="624,216 762,354 624,492 486,354" fill="url(#hedges)"
               role="img" aria-label="Photo of a formal garden path between clipped hedges"/>
      <polygon points="936,200 1070,345 936,490 798,345" fill="url(#lighthouse)"
               role="img" aria-label="Photo of a white lighthouse above green shrubs"/>
      <polygon points="780,354 918,492 780,630 642,492" fill="url(#borders)"
               role="img" aria-label="Photo of topiary and pink flower borders"/>
    </g>
  </svg>

  <div class="brand">
    <div class="brand-dot"></div>
    <p class="brand-name">Harbor Fern KT</p>
  </div>

  <p class="brand-ghost">Harbor Fern KT</p>

  <p class="offer">Call For&nbsp; A No Obligation<br>Free Job Estimate</p>
</main>
</body>
</html>
```